Discreet simple classy for adult entertainment

I would like a matte black business card with gold writing for my business. Keeping it simple. Having my following:

Lina frost
Events. Entertainment. Promotions
0477250618

or alternatively could have what i had on my previous card below but i think i prefer the above as again - discretion.

Maybe a nice gold line thru the card or some other very simple design . Or not open to ideas/ can be doublesided if any good ideas with that.

included pics of my old bus card. not sure weather i want a photo on it or not. if i do it wont be the same pic. i kinda wanted a card that was discreet so if it was in someones wallet they wouldn't neccessarily realise it was from a stripper.

Target Market(s)

men

Industry/Entity Type

Business

Contact Information for Business Card

Lina frost
0477250618

Requirements
Nice to have
• i don't know i am really open to anything. im giving my cards to guys so something they can have in their wallet that is discreet preferably.

```html
<!DOCTYPE html>
<html lang="en">
<head>
<meta charset="utf-8">
<title>Lina Frost — Business Card</title>
<link rel="stylesheet" href="https://fonts.googleapis.com/css2?family=Barlow:wght@400;500&display=swap">
<style>
  :root {
    --backdrop: #d3d8d7;
    --card-black: #050505;
    --gold: #9c7d24;
    --gold-soft: #8a6d1f;
  }
  * { margin: 0; padding: 0; box-sizing: border-box; }
  html, body {
    width: 1200px;
    height: 823px;
    overflow: hidden;
    background: var(--backdrop);
  }
  .canvas {
    position: relative;
    width: 1200px;
    height: 823px;
  }
  .business-card {
    position: absolute;
    left: 180px;
    top: 171px;
    width: 840px;
    height: 480px;
    background: var(--card-black);
    font-family: "Barlow", "DIN Alternate", Arial, sans-serif;
    color: var(--gold);
  }
  .card-frame {
    position: absolute;
    inset: 16px;
    border: 2px solid var(--gold);
  }
  .identity {
    position: absolute;
    left: 150px;
    top: 132px;
    display: inline-block;
  }
  .name {
    font-size: 90px;
    font-weight: 400;
    letter-spacing: 6px;
    line-height: 1;
    text-transform: uppercase;
    white-space: nowrap;
  }
  .name-rule {
    height: 2px;
    background: var(--gold);
    margin-top: 8px;
  }
  .services {
    margin-top: 6px;
    font-size: 26px;
    font-weight: 400;
    letter-spacing: 1.5px;
    color: var(--gold-soft);
    white-space: nowrap;
  }
  .contact {
    position: absolute;
    left: 310px;
    top: 318px;
    text-align: left;
  }
  .phone {
    font-size: 22px;
    letter-spacing: 2px;
    color: var(--gold-soft);
  }
  .contact-mark {
    display: block;
    margin: 8px 0 0 34px;
  }
</style>
</head>
<body>
  <main class="canvas">
    <section class="business-card" aria-label="Lina Frost business card">
      <div class="card-frame"></div>
      <div class="identity">
        <h1 class="name">Lina Frost</h1>
        <div class="name-rule"></div>
        <p class="services">Events | Entertainment | Promotions</p>
      </div>
      <div class="contact">
        <p class="phone">(047)-725-0618</p>
        <svg class="contact-mark" width="16" height="16" viewBox="0 0 16 16" aria-hidden="true">
          <circle cx="8" cy="8" r="6.5" fill="none" stroke="#8a6d1f" stroke-width="1.5"/>
        </svg>
      </div>
    </section>
  </main>
</body>
</html>
```